Brand New Africa Focused Specialty Insurance business needs a slick website

Meridian Cover Partners needs a slick website design to launch our business with. we have 3 lines of business to begin with - Political Risk and Trade Credit and Property. (this will extend to 9: Political violence and Terrorism, Construction, Liability, Energy, Aviation, Marine, Parametric and Crisis Management at a later date). We are based in London but are Africa focused and our mission statement Meridian Cover Partners provides comprehensive, bespoke insurance risk mitigating solutions to local and global customers, giving them the confidence to grow their businesses sustainably. our tagline is "protecting Africa". Our colours are purple (Red 36, Green 11, Blue 96) and gold (Red 143, Green 137, Blue 53).

Target Market(s)

Brokers
Businesses across africa

Coding

Number of Pages Required

4 page

Font styles to use
Sans Serif
Other font styles liked:
• Cairo (but open to others too)

Requirements
Must have
• Pages:
1. Home page/about us (to include Lines of Business)
2. a page for Property line (we will need to add a link so that people can send an email to the mailbox)
3. a page for Political Risk and Trade Credit ( we will need to add a link so that people can send an email to the mailbox)
3. a page about our people (photos not yet taken for this)
4. a careers page
we have a lot of text for the above, we just need to fine tune it

must be tied to the colour scheme I detailed above.

the font for the logo is called Cairo
Nice to have
• https://www.tolvane-mu.com/ - we like the look of this website, but perhaps less colour
Should not have
• Any African animal like Lions or Zebras

```html
<!DOCTYPE html>
<html lang="en">
<head>
<meta charset="utf-8">
<title>Meridian Cover Partners — Protecting Africa</title>
<link rel="stylesheet" href="https://fonts.googleapis.com/css2?family=Cairo:wght@400;600;700&display=swap">
<style>
:root{
  --purple:#240b60;
  --purple-deep:#2a1377;
  --gold:#8f8935;
  --gold-light:#a6a04a;
  --ink:#3a3550;
  --muted:#5a5670;
  --pale:#eceef8;
  --white:#ffffff;
}
*{box-sizing:border-box;margin:0;padding:0}
html,body{width:1200px;height:3151px;overflow:hidden}
body{position:relative;font-family:"Cairo",sans-serif;color:var(--ink);background:var(--white)}
.abs{position:absolute}

/* header */
.brand{position:absolute;display:flex;align-items:center;gap:10px}
.brand-dot{width:64px;height:64px;border-radius:50%;border:2px solid var(--gold);flex:none}
.brand-name{font-weight:700;font-size:17px;line-height:1.1;color:var(--purple)}
.brand-tag{font-weight:600;font-size:11px;color:var(--purple);display:block;margin-top:2px}
.main-nav{position:absolute;left:401px;top:35px;width:799px;height:64px;background:var(--purple);border-radius:32px 0 0 32px;z-index:3}
.main-nav a{position:absolute;top:0;line-height:64px;color:#fff;text-decoration:none;font-size:16px;transform:translateX(-50%);white-space:nowrap}
.main-nav a.active{font-weight:700}
.main-nav a.active::after{content:"";position:absolute;left:0;right:0;bottom:0;height:3px;background:var(--gold)}
.nav-sep{position:absolute;left:673px;top:23px;width:1px;height:14px;background:#6b5a9c}

/* hero */
.hero{position:absolute;left:0;top:0;width:1200px;height:667px;background:linear-gradient(180deg,#e6ebef 0%,#d4dde3 45%,#c6d6d9 100%)}
.hero-map{position:absolute;left:575px;top:140px;width:570px;height:569px;border-radius:48% 40% 45% 55% / 35% 38% 62% 55%;background:linear-gradient(160deg,#8f8935,#6f6a2a);opacity:.92;z-index:2}
.hero-eyebrow{position:absolute;left:102px;top:246px;font-weight:700;font-size:32px;color:var(--purple);line-height:1.3}
.hero-title{position:absolute;left:100px;top:285px;font-weight:700;font-size:45px;color:var(--purple);line-height:1.3}
.bar{position:absolute;height:4px;background:var(--gold)}
.hero-text{position:absolute;left:102px;top:378px;width:460px;font-size:14.5px;line-height:27px;color:var(--ink);text-transform:uppercase}
.btn-gold{position:absolute;background:var(--gold);color:#fff;font-weight:700;text-align:center;text-decoration:none}
.slider-dots{position:absolute;left:554px;top:635px;display:flex;gap:9px;z-index:3}
.slider-dots span{width:33px;height:3px;background:#8a7fb0}
.slider-dots span.on{background:var(--purple)}
.arrow{position:absolute;top:322px;z-index:3}

/* about */
.people-photo{position:absolute;left:111px;top:795px;width:431px;height:320px;background:linear-gradient(135deg,#d9b48a,#8b5a3c 45%,#c9a43a 75%,#5d7ab0);box-shadow:0 20px 40px rgba(0,0,0,.18);z-index:2}
.section-title{position:absolute;font-weight:700;color:var(--purple);line-height:1.2}
.about-text{position:absolute;left:615px;top:877px;width:498px;font-size:15px;line-height:27px;color:var(--muted);text-align:justify}
.btn-outline{position:absolute;border:2px solid var(--purple);color:var(--purple);font-weight:700;text-align:center;text-decoration:none}

/* lines of business */
.lob{position:absolute;left:0;top:1256px;width:1200px;height:556px;background:linear-gradient(180deg,#e3e5f5 0%,#e9eaf2 40%,#dfe1ea 100%)}
.lob-icon{position:absolute;width:148px;height:148px;border-radius:50%;border:3px solid var(--gold);background:rgba(255,255,255,.55);display:flex;align-items:center;justify-content:center}
.lob-icon .inner{width:118px;height:118px;border-radius:50%;background:#fff;display:flex;align-items:center;justify-content:center}
.lob-name{position:absolute;font-weight:700;font-size:24px;color:var(--purple);text-align:center;transform:translateX(-50%);white-space:nowrap}
.btn-small{position:absolute;width:137px;height:37px;line-height:33px;border:2px solid var(--gold);color:var(--purple);font-weight:700;font-size:13px;text-align:center;text-decoration:none;transform:translateX(-50%);background:rgba(255,255,255,.4)}

/* news */
.news-photo{position:absolute;left:622px;top:1812px;width:578px;height:563px;background:linear-gradient(180deg,#9ab6d0 0%,#7c7a5a 30%,#8a7d5c 55%,#b9b3a6 75%,#3f7f9a 100%)}
.news-item{position:absolute;left:129px;width:420px}
.news-date{font-size:16px;color:var(--gold);line-height:1.2}
.news-title{font-weight:600;font-size:18px;color:var(--purple);margin-top:9px;line-height:1.2}
.news-text{font-size:14.5px;line-height:27px;color:var(--muted);margin-top:4px}
.news-more{display:inline-block;margin-top:6px;font-weight:700;font-size:14px;color:var(--purple);text-decoration:none}

/* contact */
.contact{position:absolute;left:0;top:2375px;width:1200px;height:553px;background:linear-gradient(180deg,#2e1a7a,#2a1570)}
.contact-line{position:absolute;left:175px;font-size:17px;line-height:28px;color:#e8e4f6}
.contact-sep{position:absolute;left:158px;width:1px;background:#6b5aa8}
.social{position:absolute;top:2740px;left:122px;display:flex;gap:4px}
.social span{width:33px;height:32px;border:1px solid #d8d2f0}
.form-title{position:absolute;left:537px;top:2494px;font-weight:600;font-size:17px;color:#e8e4f6}
.field{position:absolute;border:1px solid #8a7fc0;color:#c9c2e6;font-size:11px;padding-left:17px}
.btn-send{position:absolute;left:543px;top:2788px;width:153px;height:49px;line-height:49px;background:var(--gold-light);color:#fff;font-weight:700;font-size:18px;text-align:center}

/* footer */
.footer-links a{position:absolute;top:3045px;font-weight:700;font-size:12.5px;color:var(--purple);text-decoration:none;transform:translateX(-50%);white-space:nowrap}
.copyright{position:absolute;left:0;width:1200px;top:3087px;text-align:center;font-size:12.5px;color:var(--muted)}
</style>
</head>
<body>

<!-- HERO -->
<section class="hero" role="img" aria-label="Aerial photograph of a coastal African city with a stadium and harbour, softly faded"></section>
<div class="hero-map" role="img" aria-label="Gold map of the African continent"></div>

<div class="brand" style="left:73px;top:37px;z-index:3">
  <span class="brand-dot"></span>
  <span><span class="brand-name">Meridian Cover Partners</span><span class="brand-tag">Protecting Africa</span></span>
</div>

<nav class="main-nav">
  <a class="active" href="#" style="left:95px">HOME</a>
  <a href="#" style="left:234px">ABOUT US</a>
  <a href="#" style="left:426px">LINE OF BUSINESS
    <svg width="12" height="8" viewBox="0 0 12 8" style="margin-left:4px"><path d="M1 1l5 5 5-5" fill="none" stroke="#fff" stroke-width="1.8"/></svg></a>
  <a href="#" style="left:593px">CAREER</a>
  <span class="nav-sep"></span>
  <a href="#" style="left:707px">
    <svg width="14" height="14" viewBox="0 0 14 14"><circle cx="6" cy="6" r="4.5" fill="none" stroke="#fff" stroke-width="2"/><path d="M9.5 9.5l3 3" stroke="#fff" stroke-width="2"/></svg></a>
</nav>

<svg class="arrow" style="left:28px" width="26" height="46" viewBox="0 0 26 46"><path d="M22 3L5 23l17 20" fill="none" stroke="#240b60" stroke-width="5"/></svg>
<svg class="arrow" style="left:1146px" width="26" height="46" viewBox="0 0 26 46"><path d="M4 3l17 20L4 43" fill="none" stroke="#240b60" stroke-width="5"/></svg>

<div class="hero-eyebrow" style="z-index:3">MERIDIAN COVER PARTNERS</div>
<h1 class="hero-title" style="z-index:3">PROTECTING AFRICA</h1>
<span class="bar" style="left:103px;top:353px;width:62px"></span>
<p class="hero-text">Lorem ipsum dolor sit amet, consectetur adipiscing elit, sed do eiusmod tempor incididunt ut</p>
<a class="btn-gold" href="#" style="left:101px;top:455px;width:164px;height:44px;line-height:44px;font-size:17px">READ MORE</a>
<div class="slider-dots"><span></span><span></span><span class="on"></span></div>

<!-- ABOUT -->
<svg class="abs" style="left:62px;top:998px" width="236" height="176" viewBox="0 0 236 176" aria-hidden="true">
  <defs><pattern id="dotgrid" width="15.4" height="15.4" patternUnits="userSpaceOnUse"><circle cx="3" cy="3" r="2.3" fill="#d6d6dc"/></pattern></defs>
  <rect width="236" height="176" fill="url(#dotgrid)"/>
</svg>
<div class="people-photo" role="img" aria-label="Photograph of a group joining hands in a circle, viewed from below"></div>

<h2 class="section-title" style="left:615px;top:793px;font-size:37px">ABOUT OUR PEOPLE</h2>
<span class="bar" style="left:616px;top:849px;width:63px"></span>
<p class="about-text">Lorem ipsum dolor sit amet, consectetur adipiscing elit, sed do eiusmod tempor incididunt ut labore et dolore magna aliqua. Ut enim ad minim veniam, quis nostrud exercitation ullamco laboris nisi ut aliquip ex<br>Aa commodo consequat. Duis aute irure dolor in reprehenderit in voluptate velit esse cillum dolore eu fugiat nulla pariatur. Excepteur sint occaecat cupidatat non proident, sunt in culpa qui officia</p>
<a class="btn-outline" href="#" style="left:615px;top:1071px;width:166px;height:45px;line-height:41px;font-size:17px">READ MORE</a>

<!-- LINES OF BUSINESS -->
<section class="lob" role="img" aria-label="Faded photograph of a city skyline behind the lines of business"></section>
<h2 class="section-title" style="left:0;width:1200px;text-align:center;top:1318px;font-size:37px">LINES OF BUSINESS</h2>
<span class="bar" style="left:565px;top:1374px;width:63px"></span>

<div class="lob-icon" style="left:283px;top:1416px"><div class="inner">
  <svg width="62" height="62" viewBox="0 0 62 62"><circle cx="31" cy="31" r="28" fill="none" stroke="#240b60" stroke-width="3"/>
  <path d="M18 14c6 2 8 6 6 10s-6 3-7 8 5 8 3 13M36 10c-2 5 2 7 6 8s6 6 3 10-2 9 3 12M14 36c5 0 8 3 10 8" fill="none" stroke="#240b60" stroke-width="3" stroke-linecap="round"/></svg>
</div></div>
<div class="lob-icon" style="left:759px;top:1416px"><div class="inner">
  <svg width="76" height="66" viewBox="0 0 76 66" fill="none" stroke="#240b60" stroke-width="2.6">
    <rect x="4" y="18" width="16" height="46"/><rect x="22" y="4" width="24" height="60"/><rect x="48" y="12" width="22" height="52"/>
    <path d="M12 10v8M8 26h8M8 34h8M8 42h8M8 50h8M28 12h12M28 22h12M28 32h12M28 42h12M28 52h12M54 22h10M54 32h10M54 42h10M54 52h10M2 64h72"/></svg>
</div></div>

<div class="lob-name" style="left:352px;top:1584px">POLITICAL RISK AND TRADE CREDIT</div>
<div class="lob-name" style="left:845px;top:1584px">PROPERTY</div>
<a class="btn-small" href="#" style="left:353px;top:1642px">READ MORE</a>
<a class="btn-small" href="#" style="left:845px;top:1638px">READ MORE</a>

<!-- NEWS -->
<h2 class="section-title" style="left:132px;top:1880px;font-size:38px">AFRICA NEWS</h2>
<span class="bar" style="left:133px;top:1933px;width:64px"></span>

<article class="news-item" style="top:1979px">
  <div class="news-date">AUGUST 19</div>
  <div class="news-title">LOREM IPSUM DOLOR SIT AMET</div>
  <p class="news-text">consectetur adipiscing elit, sed do eiusmod tempor incididunt ut labore et dolore magna aliqua. Ut enim ad minim veniamex</p>
  <a class="news-more" href="#">LEARN MORE &#8594;</a>
</article>
<article class="news-item" style="top:2169px">
  <div class="news-date">AUGUST 20</div>
  <div class="news-title">LOREM IPSUM DOLOR SIT AMET</div>
  <p class="news-text">consectetur adipiscing elit, sed do eiusmod tempor incididunt ut labore et dolore magna aliqua. Ut enim ad minim veniamex</p>
  <a class="news-more" href="#">LEARN MORE &#8594;</a>
</article>
<div class="news-photo" role="img" aria-label="Aerial photograph of a coastal city beneath a flat-topped mountain"></div>

<!-- CONTACT -->
<section class="contact" role="img" aria-label="Purple panel with a faint savanna landscape photograph"></section>
<h2 class="section-title" style="left:123px;top:2483px;font-size:38px;color:#fff">CONTACT US</h2>
<span class="bar" style="left:125px;top:2534px;width:66px;background:var(--gold-light)"></span>

<svg class="abs" style="left:122px;top:2590px" width="22" height="30" viewBox="0 0 22 30"><path d="M11 1C5.5 1 1 5.3 1 10.8 1 18 11 29 11 29s10-11 10-18.2C21 5.3 16.5 1 11 1z" fill="#a6a04a"/><circle cx="11" cy="10.5" r="3.8" fill="#2c1776"/></svg>
<span class="contact-sep" style="top:2586px;height:42px"></span>
<div class="contact-line" style="top:2579px">Harrow Court, 12-14 Fenwick Lane,<br>London, EC3A 9QT</div>

<svg class="abs" style="left:122px;top:2659px" width="24" height="17" viewBox="0 0 24 17"><rect width="24" height="17" fill="#a6a04a"/><path d="M0 0l12 9 12-9" fill="none" stroke="#2c1776" stroke-width="1.8"/></svg>
<span class="contact-sep" style="top:2651px;height:32px"></span>
<div class="contact-line" style="top:2654px">contact@meridiancover.com</div>

<div class="social" aria-label="Social links"><span></span><span></span><span></span><span></span></div>

<div class="form-title">FOR ANY QUESTIONS SEND US A MESSAGE</div>
<div class="field" style="left:541px;top:2541px;width:257px;height:39px;line-height:39px">FIRST NAME*</div>
<div class="field" style="left:806px;top:2541px;width:257px;height:39px;line-height:39px">LAST NAME*</div>
<div class="field" style="left:541px;top:2592px;width:522px;height:38px;line-height:38px">E-MAIL*</div>
<div class="field" style="left:541px;top:2644px;width:522px;height:132px;padding-top:12px">YOUR MESSAGE</div>
<div class="btn-send">SEND</div>

<!-- FOOTER -->
<div class="brand" style="left:484px;top:2962px">
  <span class="brand-dot"></span>
  <span><span class="brand-name">Meridian Cover Partners</span><span class="brand-tag">Protecting Africa</span></span>
</div>
<nav class="footer-links">
  <a href="#" style="left:289px">HOME</a>
  <a href="#" style="left:379px">ABOUT US</a>
  <a href="#" style="left:499px">PROPERTY LINE</a>
  <a href="#" style="left:633px">POLITICAL RISK</a>
  <a href="#" style="left:780px">ABOUT OUR PEOPLE</a>
  <a href="#" style="left:905px">CAREER</a>
</nav>
<p class="copyright">© Meridian Cover Partners 2020 | &nbsp;All Rights Reserved</p>

</body>
</html>
```